Real Estate Business Card

On the front side I want to have my info, my brokerage info.
On the back side I want have my complany’s logo, website and Facebook link. I will provide all this once I select a design.

I would like to see Black background and gold text, Dark Blue and gold text and White and blue text designs

Font styles to use
Sans Serif
Script

```html
<!DOCTYPE html>
<html lang="en">
<head>
<meta charset="utf-8">
<title>Harbour Lane – Business Card</title>
<link href="https://fonts.googleapis.com/css2?family=Cinzel:wght@600&family=Open+Sans:wght@400&display=swap" rel="stylesheet">
<style>
  :root {
    --stage: #5c5c5c;
    --card-navy: #12325a;
    --pattern-navy: #17395f;
    --gold: #f0c232;
    --text-light: #e9edf3;
    --rule: #3a5577;
  }
  * { box-sizing: border-box; margin: 0; padding: 0; }
  html, body { width: 1200px; height: 802px; overflow: hidden; }
  body {
    background: var(--stage);
    position: relative;
    font-family: "Open Sans", sans-serif;
    color: var(--text-light);
  }
  .card {
    position: absolute;
    top: 274px;
    width: 443px;
    height: 265px;
    background: var(--card-navy);
    box-shadow: 2px 3px 6px rgba(0,0,0,.45);
    overflow: hidden;
  }
  .card--front { left: 136px; }
  .card--back  { left: 624px; }

  .brand-name {
    position: absolute;
    left: 20px;
    width: 198px;
    top: 118px;
    text-align: center;
    font-family: "Cinzel", serif;
    font-weight: 600;
    font-size: 26px;
    line-height: 1.05;
    color: var(--gold);
  }
  .divider {
    position: absolute;
    left: 227px;
    top: 68px;
    width: 1px;
    height: 132px;
    background: var(--rule);
  }
  .contact {
    position: absolute;
    left: 241px;
    top: 60px;
  }
  .contact__name {
    font-family: "Cinzel", serif;
    font-weight: 600;
    font-size: 18px;
    color: var(--gold);
    letter-spacing: .3px;
    line-height: 22px;
  }
  .contact__role { font-size: 12.5px; line-height: 16px; margin-bottom: 6px; }
  .contact__line {
    display: flex;
    align-items: center;
    gap: 5px;
    font-size: 12.5px;
    line-height: 16px;
  }
  .contact__line svg { width: 11px; height: 11px; fill: var(--gold); flex: none; }
  .contact__address { font-size: 12.5px; line-height: 16px; margin-top: 4px; }
  .website {
    position: absolute;
    left: 0; right: 0;
    top: 226px;
    text-align: center;
    font-size: 12.5px;
  }

  .back-pattern {
    position: absolute;
    inset: 0;
    background: linear-gradient(180deg, var(--pattern-navy), var(--card-navy));
  }
  .back-brand {
    position: absolute;
    left: 310px;
    top: 140px;
    font-family: "Cinzel", serif;
    font-weight: 600;
    font-size: 14px;
    color: var(--gold);
  }
  .social {
    position: absolute;
    left: 0; right: 0;
    top: 229px;
    text-align: center;
    font-size: 11.5px;
  }
</style>
</head>
<body>
  <section class="card card--front">
    <div class="brand-name">HARBOUR<br>LANE</div>
    <div class="divider"></div>
    <div class="contact">
      <p class="contact__name">DANIEL CARTER</p>
      <p class="contact__role">Managing Director</p>
      <p class="contact__line">
        <svg viewBox="0 0 12 12" aria-hidden="true"><path d="M1 4c0-2 2-3 5-3s5 1 5 3v1H8V4H4v1H1z M3 6h6l1 5H2z"/></svg>044-555 010 247
      </p>
      <p class="contact__line">
        <svg viewBox="0 0 12 12" aria-hidden="true"><path d="M3 0h6v12H3z M4 1.5v8h4v-8z"/></svg>044-555 010 247
      </p>
      <p class="contact__line">
        <svg viewBox="0 0 12 12" aria-hidden="true"><path d="M3 0h6v4H3z M1 4h10v5H1z M3 8h6v4H3z"/></svg>044-555 010 247
      </p>
      <p class="contact__line">
        <svg viewBox="0 0 12 12" aria-hidden="true"><path d="M0 2h12v8H0z" /><path d="M0 2l6 4 6-4" fill="none" stroke="#12325a" stroke-width="1"/></svg>hello@harbourlane.com
      </p>
      <p class="contact__address">48 Ridge Road, Oakvale<br>Northland, 204817.</p>
    </div>
    <p class="website">www.harbourlane.com</p>
  </section>

  <section class="card card--back">
    <div class="back-pattern" role="img" aria-label="Faint repeating brand pattern across the card back"></div>
    <div class="back-brand">HARBOUR LANE</div>
    <p class="social">www.friendsite.com/harbourlane</p>
  </section>
</body>
</html>
```